Business Card Design for a Personal Trainer

I need a business card design for my job as a personal trainer. It should have a unique, modern and exclusive design. On the front there should be only my logo with my name and my job. 0163/2918374 Tobias Hellwig Lindenkopfweg 14 80921 Munich Germany The most important contact information is the web adress. it can be bigger than the rest, but its not necessary. The card should be 8,5cmx5,5cm big. Font: Roboto. Colors: black, white, gray, 56c1ff.

```html
<!DOCTYPE html>
<html lang="de">
<head>
<meta charset="utf-8">
<title>Tobias Hellwig – Personal Trainer Visitenkarte</title>
<link rel="stylesheet" href="https://fonts.googleapis.com/css2?family=Roboto:wght@300;400;500&family=Noto+Serif:wght@700&display=swap">
<style>
  :root {
    --bg: #2a2a2c;
    --black: #111111;
    --white: #f6f6f6;
    --gray: #8a8a8a;
    --accent: #56c1ff;
    --url: #6a4fd8;
    --sky-top: #7c7aa0;
    --sky-mid: #b8b4cc;
    --sky-low: #4c3f72;
  }
  * { margin: 0; padding: 0; box-sizing: border-box; }
  html, body { width: 1200px; height: 923px; overflow: hidden; }
  body {
    background: var(--bg);
    font-family: "Roboto", Arial, sans-serif;
    position: relative;
  }
  .card {
    position: absolute;
    left: 280px;
    width: 640px;
    height: 414px;
    overflow: hidden;
    box-shadow: 0 10px 30px rgba(0,0,0,.45);
  }
  .card--front { top: 30px; }
  .card--back { top: 479px; background: var(--white); }

  /* front */
  .front-photo {
    position: absolute; inset: 0;
    background: linear-gradient(180deg, var(--sky-top) 0%, var(--sky-mid) 45%, var(--sky-low) 75%, #2f2a45 100%);
  }
  .front-logo {
    position: absolute; left: 0; right: 0; top: 120px;
    display: flex; flex-direction: column; align-items: center;
  }
  .brand { display: flex; align-items: center; gap: 14px; }
  .brand__mark { width: 34px; height: 34px; background: var(--black); }
  .brand__name {
    font-size: 36px; font-weight: 400; color: var(--black);
    letter-spacing: 1px; text-transform: uppercase;
  }
  .brand__role {
    margin-top: 6px; padding: 0 18px;
    font-size: 13px; letter-spacing: 5px; color: var(--black);
    text-transform: uppercase;
    border-top: 1px solid var(--black);
    border-bottom: 1px solid var(--black);
  }

  /* back */
  .back-photo {
    position: absolute; top: 0; right: 0; width: 300px; height: 100%;
    background: linear-gradient(90deg, rgba(246,246,246,0) 0%, #9a9a9a 35%, #3a3a3a 70%, #0d0d0d 100%);
  }
  .back-frame { position: absolute; left: 0; top: 0; }
  .back-logo {
    position: absolute; left: 95px; top: 95px; width: 300px;
    display: flex; flex-direction: column; align-items: center;
  }
  .back-logo .brand__name { font-size: 28px; }
  .back-logo .brand__mark { width: 26px; height: 26px; }
  .back-logo .brand__role { font-size: 11px; letter-spacing: 4px; }
  .contact {
    position: absolute; left: 95px; top: 230px; width: 300px;
    border-top: 1px solid var(--black);
    padding-top: 14px;
    text-align: center;
  }
  .contact__name {
    font-family: "Noto Serif", Georgia, serif;
    font-size: 26px; font-weight: 700; color: var(--accent);
  }
  .contact__web { font-size: 19px; color: var(--url); margin-top: 4px; }
  .contact__line { font-size: 15px; color: var(--black); margin-top: 6px; font-weight: 300; }
</style>
</head>
<body>
  <section class="card card--front">
    <div class="front-photo" role="img" aria-label="Foto: Trainer von hinten am Meer bei violettem Wolkenhimmel"></div>
    <div class="front-logo">
      <div class="brand">
        <span class="brand__mark"></span>
        <span class="brand__name">Tobias Hellwig</span>
      </div>
      <div class="brand__role">Personal Trainer</div>
    </div>
  </section>

  <section class="card card--back">
    <div class="back-photo" role="img" aria-label="Schwarz-weiß Porträt des Trainers mit verschränkten Armen"></div>
    <svg class="back-frame" width="640" height="414" viewBox="0 0 640 414">
      <path d="M40 110 V50 H100" fill="none" stroke="var(--black)" stroke-width="10"/>
      <line x1="62" y1="60" x2="62" y2="390" stroke="var(--black)" stroke-width="1.5"/>
      <line x1="220" y1="45" x2="340" y2="45" stroke="var(--black)" stroke-width="1.5"/>
    </svg>
    <div class="back-logo">
      <div class="brand">
        <span class="brand__mark"></span>
        <span class="brand__name">Tobias Hellwig</span>
      </div>
      <div class="brand__role">Personal Trainer</div>
    </div>
    <div class="contact">
      <div class="contact__name">Tobias Hellwig</div>
      <div class="contact__web">www.tobiashellwig.de</div>
      <div class="contact__line">0163/2918374</div>
      <div class="contact__line">t.hellwig@postfach-mail.de</div>
      <div class="contact__line">Lindenkopfweg 14, 80921 München</div>
    </div>
  </section>
</body>
</html>
```